Profesional personal website needs design and business card

I need a business card with my professional name as a logo "Marlo Vitality" for my business. I am a Wellness Coach, consultant and trainer. So it should be professional, wellness oriented and modern.

Target Market(s)

Private clients, governments, corporations. Luxury and high market.

Industry/Entity Type

Health And Wellness

Contact Information for Business Card

Marlo Vitality should be the logo

Colors

Designer to choose colors to be used in the design.

Requirements
Must have
• Marlo Vitality
• Name: Tomás Arribal
• Wellness Coach, Consultant & Trainer.
• Website: www.marlovitality.example
• Phone:
• Spain (+34) 612 480 397
• (USA) +1 (555) 318 2046
Nice to have
• The most important is the design of "Marlo Vitality", as this is going to be my personal brand logo. It should be professional, wellness, high end and actual.
Should not have
• no golds, no baroque style..

```html
<!DOCTYPE html>
<html lang="en">
<head>
<meta charset="utf-8">
<title>Marlo Vitality — Business Card</title>
<link rel="stylesheet" href="https://fonts.googleapis.com/css2?family=Questrial&display=swap">
<style>
  :root {
    --bg: #b9b9b9;
    --card: #2a2a2a;
    --card-deep: #232323;
    --accent: #f26f1f;
    --ink: #f2f2f2;
    --ink-soft: #cfcfcf;
  }
  * { box-sizing: border-box; margin: 0; padding: 0; }
  html, body {
    width: 1200px; height: 1000px; overflow: hidden;
    background: var(--bg);
    font-family: "Questrial", "Century Gothic", sans-serif;
  }
  .canvas {
    width: 1200px; height: 1000px;
    display: flex; flex-direction: column; align-items: center; justify-content: center;
    gap: 56px;
  }
  .card {
    position: relative;
    width: 735px; height: 420px;
    background: var(--card);
    border: 4px solid var(--accent);
    border-radius: 3px;
    overflow: hidden;
  }
  .brand-name {
    color: var(--ink);
    text-align: center;
    font-weight: 400;
    letter-spacing: 2px;
  }
  .card--front { display: flex; align-items: center; justify-content: center; }
  .card--front .brand-name { font-size: 54px; margin-top: -40px; }

  .card--back .brand-name {
    position: absolute; top: 34px; left: 0; right: 0;
    font-size: 34px;
  }
  .identity {
    position: absolute; left: 0; width: 50%; top: 150px;
    text-align: center;
  }
  .person-name {
    color: var(--accent);
    font-size: 32px; letter-spacing: 1.5px;
    font-weight: 400;
  }
  .person-role {
    margin-top: 10px;
    color: var(--ink-soft);
    font-size: 12.5px; font-style: italic; letter-spacing: .6px;
  }
  .person-role .sep { display: inline-block; width: 1px; height: 13px; background: var(--ink-soft); margin: 0 5px; vertical-align: -2px; }
  .divider {
    position: absolute; left: 50%; top: 140px;
    width: 2px; height: 88px; background: var(--accent);
  }
  .contact {
    position: absolute; left: 50%; right: 0; top: 112px;
    text-align: center;
    color: var(--ink-soft);
    font-size: 16.5px; letter-spacing: .8px; line-height: 30px;
  }
  .contact svg { display: block; margin: 0 auto 12px; }
  .web-band {
    position: absolute; left: 0; right: 0; bottom: 46px;
    height: 32px; background: var(--accent);
    color: #fff; text-align: center;
    font-size: 18px; letter-spacing: 1.5px; line-height: 32px;
  }
  .card--back::after {
    content: ""; position: absolute; left: 0; right: 0; bottom: 0; height: 46px;
    background: var(--card-deep);
  }
</style>
</head>
<body>
<main class="canvas">
  <section class="card card--front">
    <h1 class="brand-name">Marlo Vitality</h1>
  </section>

  <section class="card card--back">
    <h2 class="brand-name">Marlo Vitality</h2>
    <div class="identity">
      <p class="person-name">Tomás Arribal</p>
      <p class="person-role">Wellness Coach<span class="sep"></span>Consultant &amp; Trainer</p>
    </div>
    <div class="divider"></div>
    <div class="contact">
      <svg width="26" height="26" viewBox="0 0 24 24" aria-hidden="true">
        <path fill="#f26f1f" d="M6.6 10.8c1.4 2.8 3.8 5.1 6.6 6.6l2.2-2.2c.3-.3.7-.4 1-.2 1.1.4 2.3.6 3.6.6.6 0 1 .4 1 1V20c0 .6-.4 1-1 1C10.6 21 3 13.4 3 4c0-.6.4-1 1-1h3.5c.6 0 1 .4 1 1 0 1.3.2 2.5.6 3.6.1.3 0 .7-.2 1l-2.3 2.2z"/>
      </svg>
      <p>Spain (+34) 612 480 397</p>
      <p>(USA) +1 (555) 318 2046</p>
    </div>
    <div class="web-band">www.marlovitality.example</div>
  </section>
</main>
</body>
</html>
```